Professional Business Card for Commercial Cleaning Company

We need a business card that represents our commercial janitorial cleaning company and represent several brands for our company so we do not want to highlight the logo too much. We want something that says we are professional.
Notes:No website or address as we have many locations and many websites and companies under our corporate name of "Brightmere Holdings, LLC" . Every time we hand a customer a business card they have contacted us via another brand we own but we don't want to have 21 business cards so we want to not focus on Brightmere Holdings, LLC too much since people will automatically ask "What is Brightmere Holdings, LLC" Example: Noodle Barn and Wrap Lodge restaurants are owned by "Zest! Brands" is the corporation name. Same principle here. Except we do not advertise at this time that all of our brands are connected. Hope this helps.
Target Market(s)
Commercial Cleaning
Industry/Entity Type
Janitorial Service
Contact Information for Business Card
Miles Penrow
Business Development
482-639-2274
sales@brightmereholdingsllc.example
Requirements
Must have
- Logo with contact information, need to be able to easily edit contact info for others in my office.
Nice to have
- Professional Image. Like to see a colorful bold look and a more standard business card look.
Should not have
- Any type of cleaning icons, tools, people or water.

```html
<!DOCTYPE html>
<html lang="en">
<head>
<meta charset="utf-8">
<title>Brightmere Holdings, LLC — Business Card</title>
<link rel="stylesheet" href="https://fonts.googleapis.com/css2?family=Montserrat:wght@600&family=Mulish:wght@400;700&display=swap">
<style>
  :root {
    --navy: #172f66;
    --green: #4a9a2f;
    --white: #ffffff;
    --grey-text: #5b6170;
    --backdrop: #e8e9ec;
    --divider: #2b3f73;
  }
  * { margin: 0; padding: 0; box-sizing: border-box; }
  html, body {
    width: 1200px; height: 857px; overflow: hidden;
    background: var(--backdrop);
  }
  .sheet {
    position: relative; width: 1200px; height: 857px;
    display: flex; align-items: center; justify-content: center; gap: 50px;
  }
  .card {
    position: relative; width: 525px; height: 300px; overflow: hidden;
    box-shadow: 0 6px 18px rgba(20, 30, 60, 0.18);
  }
  .card--front {
    background: var(--navy);
    display: flex; align-items: center; justify-content: center;
  }
  .card--back { background: var(--white); }

  .brand-name {
    font-family: "Montserrat", sans-serif; font-weight: 600;
    letter-spacing: -0.2px; white-space: nowrap;
  }
  .card--front .brand-name { color: var(--white); font-size: 29px; }
  .card--back .brand-name {
    position: absolute; left: 24px; top: 160px;
    color: var(--navy); font-size: 18px;
  }

  .card__waves { position: absolute; inset: 0; width: 525px; height: 300px; }

  .card__divider {
    position: absolute; left: 275px; top: 62px; width: 1px; height: 100px;
    background: var(--divider);
  }
  .contact {
    position: absolute; left: 290px; top: 62px;
    font-family: "Mulish", sans-serif; color: var(--grey-text);
  }
  .contact__name {
    font-weight: 700; font-size: 17px; color: var(--navy); line-height: 1.1;
  }
  .contact__role { font-size: 10.5px; margin-top: 3px; }
  .contact__list { list-style: none; margin-top: 20px; font-size: 10px; }
  .contact__item { display: flex; align-items: center; gap: 6px; line-height: 1.7; }
  .contact__icon { width: 10px; height: 10px; flex: none; }
</style>
</head>
<body>
<main class="sheet">
  <section class="card card--front" aria-label="Card front">
    <span class="brand-name">Brightmere Holdings, LLC</span>
  </section>

  <section class="card card--back" aria-label="Card back">
    <svg class="card__waves" viewBox="0 0 525 300" aria-hidden="true">
      <path fill="var(--green)" d="M0,266 C170,258 380,215 525,164 L525,173 C380,225 170,268 0,273 Z"/>
      <path fill="var(--navy)" d="M0,281 C170,276 380,236 525,181 L525,194 C400,250 220,300 120,300 L0,300 Z"/>
    </svg>

    <span class="brand-name">Brightmere Holdings, LLC</span>

    <div class="card__divider"></div>

    <div class="contact">
      <p class="contact__name">Miles Penrow</p>
      <p class="contact__role">Business Development</p>
      <ul class="contact__list">
        <li class="contact__item">
          <svg class="contact__icon" viewBox="0 0 24 24" aria-hidden="true">
            <path fill="var(--green)" d="M6.6 10.8a15.1 15.1 0 0 0 6.6 6.6l2.2-2.2a1 1 0 0 1 1-.25 11.4 11.4 0 0 0 3.6.57 1 1 0 0 1 1 1V20a1 1 0 0 1-1 1A17 17 0 0 1 3 4a1 1 0 0 1 1-1h3.5a1 1 0 0 1 1 1c0 1.25.2 2.45.57 3.57a1 1 0 0 1-.25 1z"/>
          </svg>
          <span>482-639-2274</span>
        </li>
        <li class="contact__item">
          <svg class="contact__icon" viewBox="0 0 24 24" aria-hidden="true">
            <rect x="2.5" y="5" width="19" height="14" rx="1.5" fill="none" stroke="var(--green)" stroke-width="2.2"/>
            <path d="M3 6l9 7 9-7" fill="none" stroke="var(--green)" stroke-width="2.2"/>
          </svg>
          <span>sales@brightmereholdingsllc.example</span>
        </li>
      </ul>
    </div>
  </section>
</main>
</body>
</html>
```